Broschüre Personalberatung
Zielgruppe
Personalberatung im technischen Umfeld für Führungskräfte und spezialisierte Experten
Aufgabenstellung
Es soll eine neue Firmenpräsentation für PDF Versand designt werden. Nur das Design der Seiten mit Kästen für Texte. Es sollen die Rauten / eckigen Kanten die um das Logo herum sind sich wieder in dem Layout wiederfinden. Die Deckseite von der angehängten Firmenpräsentation finde ich z.B. nicht schlecht. Keine Runden Elemente, gerne klare Linien wie in den Beispielen unten. Das Layout muss zum Schluss in Canva bereitgestellt werden, damit wir es auch weiter bearbeiten können. Die Farben sollen sich aus dem logo und dem generellen Auftritt wieder finden können. Stil soll seriös und professionell sein

```html
<!DOCTYPE html>
<html lang="en">
<head>
<meta charset="utf-8">
<title>Arvenhold Executive – Company Presentation Pages</title>
<link href="https://fonts.googleapis.com/css2?family=Exo+2:wght@500;600;700;800&family=Roboto:wght@300;400;500;700&display=swap" rel="stylesheet">
<style>
:root{
  --navy:#0b3a7a;
  --navy-deep:#1b2452;
  --blue:#1f5fb3;
  --teal:#2a8db8;
  --ink:#16243f;
  --grey:#8a93a3;
  --slide:#eef0f3;
  --hex-light:#dfe3e9;
  --page:#ffffff;
}
*{box-sizing:border-box;margin:0;padding:0}
html,body{width:1200px;height:805px;overflow:hidden;background:var(--page)}
body{position:relative;font-family:"Roboto",sans-serif;color:var(--ink)}
.slide{position:absolute;background:var(--slide);overflow:hidden;box-shadow:0 1px 3px rgba(20,30,60,.12)}
.slide-num{position:absolute;left:0;top:0;width:21px;height:21px;background:var(--navy);color:#fff;font:700 12px/21px "Exo 2",sans-serif;text-align:center;z-index:5}
.stripes{position:absolute;right:0;bottom:0;width:40px;height:80px;z-index:4}
.abs{position:absolute}
.h-title{font-family:"Exo 2",sans-serif;font-weight:700;color:var(--navy)}
.photo{position:absolute}
.hex-bg{position:absolute}
.icon{position:absolute}
/* slide 1 */
.brand{position:absolute;display:flex;align-items:center;gap:5px;font:600 13px "Exo 2",sans-serif;color:var(--navy);letter-spacing:.5px;white-space:nowrap}
.brand .mark{width:9px;height:9px;background:var(--navy)}
.cover-title{left:24px;top:60px;font:800 22px/1.1 "Exo 2",sans-serif;color:var(--navy)}
.cover-tag{left:27px;top:117px;font:700 11.5px/1.1 "Exo 2",sans-serif;color:var(--navy)}
.cover-sub{left:27px;top:160px;font:300 12px "Roboto",sans-serif;color:var(--teal)}
/* lists */
.fact{position:absolute;left:30px;display:flex;align-items:center;gap:9px}
.fact b{display:block;font:600 9.5px/1.15 "Exo 2",sans-serif;color:var(--navy)}
.fact span{display:block;font:600 8px/1.1 "Roboto",sans-serif;color:var(--navy)}
.strength{position:absolute;left:206px;display:flex;gap:8px;align-items:flex-start}
.strength p{font:500 6.8px/1.38 "Roboto",sans-serif;color:var(--ink);width:100px}
.challenge{position:absolute;left:30px;display:flex;gap:10px;align-items:flex-start}
.challenge p{font:500 8px/1.4 "Roboto",sans-serif;color:var(--navy);width:136px}
.pillar{position:absolute;top:48px;width:80px;text-align:center}
.pillar p{text-align:left;font:400 8px/1.2 "Roboto",sans-serif;color:var(--navy);margin-top:12px;padding-left:4px}
.vdiv{position:absolute;width:1px;background:#9fb0c8}
.resp{position:absolute;left:16px;display:flex;gap:7px;align-items:flex-start}
.resp p{font:400 6.8px/1.3 "Roboto",sans-serif;color:var(--ink);width:152px}
.benefit{position:absolute;top:42px;width:110px;text-align:center}
.benefit b{display:block;margin-top:8px;font:600 8.5px "Roboto",sans-serif;color:var(--navy)}
.benefit p{margin-top:4px;font:400 8.5px/1.65 "Roboto",sans-serif;color:var(--blue)}
.phase{position:absolute;top:37px;width:110px;text-align:center}
.phase b{display:block;margin-top:6px;font:600 8.5px "Roboto",sans-serif;color:var(--navy)}
.phase p{font:400 8.5px/1.5 "Roboto",sans-serif;color:var(--navy)}
.cta{position:absolute;left:24px;top:108px;width:112px;height:29px;background:var(--teal);color:#fff;font:600 13px/29px "Exo 2",sans-serif;text-align:center;letter-spacing:.3px;border-radius:2px}
.contact{position:absolute;left:186px;display:flex;gap:10px;align-items:flex-start;font:400 7.5px/1.45 "Roboto",sans-serif;color:var(--ink)}
.legend{position:absolute;left:290px;top:92px;font:400 8px "Roboto",sans-serif;color:var(--blue)}
.legend li{list-style:none;display:flex;align-items:center;gap:6px;height:12px}
.legend i{width:6px;height:6px;display:block}
</style>
</head>
<body>

<svg width="0" height="0" style="position:absolute" aria-hidden="true">
  <defs>
    <symbol id="hex" viewBox="0 0 100 88"><polygon points="25,2 75,2 98,44 75,86 25,86 2,44" fill="currentColor"/></symbol>
    <symbol id="hex-line" viewBox="0 0 100 88"><polygon points="25,3 75,3 97,44 75,85 25,85 3,44" fill="#fff" stroke="currentColor" stroke-width="3"/></symbol>
    <symbol id="ic-people" viewBox="0 0 100 88"><g fill="currentColor"><circle cx="50" cy="32" r="9"/><circle cx="32" cy="38" r="7"/><circle cx="68" cy="38" r="7"/><path d="M36 64c0-10 6-17 14-17s14 7 14 17z"/><path d="M20 62c0-8 5-14 12-14 4 0 6 1 8 3-4 3-6 7-6 11z"/><path d="M80 62c0-8-5-14-12-14-4 0-6 1-8 3 4 3 6 7 6 11z"/></g></symbol>
    <symbol id="ic-trend" viewBox="0 0 100 88"><g fill="none" stroke="currentColor" stroke-width="7" stroke-linejoin="round" stroke-linecap="round"><polyline points="24,62 42,44 54,54 74,32"/><polyline points="60,31 75,31 75,46"/></g></symbol>
    <symbol id="ic-shake" viewBox="0 0 100 88"><g fill="none" stroke="currentColor" stroke-width="6" stroke-linejoin="round" stroke-linecap="round"><polyline points="18,36 30,30 44,36 54,32 66,30 82,36"/><polyline points="30,30 26,54 46,66 62,58 72,50 74,34"/><line x1="44" y1="48" x2="52" y2="56"/><line x1="52" y1="44" x2="60" y2="52"/></g></symbol>
    <symbol id="ic-bars" viewBox="0 0 100 88"><g fill="currentColor"><rect x="28" y="48" width="9" height="16"/><rect x="42" y="40" width="9" height="24"/><rect x="56" y="34" width="9" height="30"/><rect x="24" y="66" width="52" height="4"/></g><polyline points="28,40 46,30 70,24" fill="none" stroke="currentColor" stroke-width="4"/></symbol>
    <symbol id="ic-calendar" viewBox="0 0 100 88"><g fill="none" stroke="currentColor" stroke-width="4"><rect x="30" y="26" width="40" height="38"/><line x1="30" y1="36" x2="70" y2="36"/></g><g fill="currentColor"><rect x="36" y="42" width="5" height="5"/><rect x="47" y="42" width="5" height="5"/><rect x="58" y="42" width="5" height="5"/><rect x="36" y="52" width="5" height="5"/><rect x="47" y="52" width="5" height="5"/></g></symbol>
    <symbol id="ic-building" viewBox="0 0 100 88"><g fill="currentColor"><rect x="32" y="24" width="22" height="42"/><rect x="56" y="36" width="14" height="30"/></g><g fill="#fff"><rect x="36" y="30" width="4" height="5"/><rect x="45" y="30" width="4" height="5"/><rect x="36" y="40" width="4" height="5"/><rect x="45" y="40" width="4" height="5"/><rect x="36" y="50" width="4" height="5"/><rect x="45" y="50" width="4" height="5"/></g></symbol>
    <symbol id="ic-chart" viewBox="0 0 100 88"><g fill="currentColor"><rect x="32" y="48" width="6" height="16"/><rect x="42" y="42" width="6" height="22"/><rect x="52" y="36" width="6" height="28"/><rect x="62" y="28" width="6" height="36"/><rect x="28" y="66" width="44" height="3"/></g></symbol>
    <symbol id="stripe" viewBox="0 0 50 100"><polygon points="41,0 50,0 12,84 3,84" fill="#1b2452"/><polygon points="50,22 50,40 24,100 10,100" fill="#2a8db8"/></symbol>
  </defs>
</svg>

<!-- 1 Cover -->
<section class="slide" style="left:50px;top:45px;width:385px;height:197px">
  <div class="slide-num">1</div>
  <svg class="hex-bg" style="left:150px;top:-20px" width="150" height="220" viewBox="0 0 150 220" aria-hidden="true"><polygon points="40,0 150,0 150,220 60,220 0,110" fill="#e4e7ec"/></svg>
  <svg class="photo" style="left:222px;top:0" width="163" height="197" viewBox="0 0 163 197" role="img" aria-label="Portrait photo of a smiling business executive in a navy suit in a bright office">
    <defs><linearGradient id="g1" x1="0" y1="0" x2="1" y2="1"><stop offset="0" stop-color="#dfe6ee"/><stop offset=".6" stop-color="#9eb0c6"/><stop offset="1" stop-color="#1d2f52"/></linearGradient></defs>
    <polygon points="45,0 163,0 163,197 18,197 0,110" fill="url(#g1)"/>
  </svg>
  <svg class="icon" style="left:205px;top:130px" width="52" height="46" aria-hidden="true"><use href="#hex" style="color:#2a8db8"/></svg>
  <div class="brand" style="left:30px;top:22px"><i class="mark"></i>Arvenhold Executive</div>
  <h1 class="abs cover-title">Main Presentation<br>Title</h1>
  <p class="abs cover-tag">Supporting statement or<br>tagline</p>
  <p class="abs cover-sub">Subtitle text here</p>
  <svg class="stripes" viewBox="0 0 50 100" aria-hidden="true"><use href="#stripe"/></svg>
</section>

<!-- 2 Strategic Direction -->
<section class="slide" style="left:444px;top:45px;width:327px;height:197px">
  <div class="slide-num">2</div>
  <svg class="hex-bg" style="left:130px;top:0" width="197" height="197" viewBox="0 0 197 197" aria-hidden="true"><polygon points="60,0 197,0 197,197 90,197 30,100" fill="#e3e6eb"/></svg>
  <h2 class="abs h-title" style="left:28px;top:56px;font-size:23px;line-height:1.1">Strategic<br>Direction</h2>
  <div class="abs" style="left:28px;top:121px;width:30px;height:2px;background:var(--blue)"></div>
  <p class="abs" style="left:28px;top:132px;font-size:10px;line-height:1.3">Building today for a<br>stronger tomorrow.</p>
  <svg class="icon" style="left:164px;top:50px" width="106" height="93" viewBox="0 0 100 88" aria-hidden="true">
    <polygon points="25,2 75,2 98,44 75,86 25,86 2,44" fill="var(--navy)" stroke="#fff" stroke-width="3"/>
    <g fill="none" stroke="#fff" stroke-width="4"><circle cx="48" cy="46" r="20"/><circle cx="48" cy="46" r="12"/></g>
    <circle cx="48" cy="46" r="4" fill="#fff"/>
    <g stroke="#fff" stroke-width="4" stroke-linecap="round" fill="none"><line x1="48" y1="46" x2="68" y2="26"/><polyline points="62,22 68,26 72,32"/></g>
  </svg>
  <svg class="stripes" viewBox="0 0 50 100" aria-hidden="true"><use href="#stripe"/></svg>
</section>

<!-- 3 Introduction -->
<section class="slide" style="left:780px;top:45px;width:375px;height:197px">
  <div class="slide-num">3</div>
  <svg class="photo" style="left:168px;top:20px" width="207" height="177" viewBox="0 0 207 177" role="img" aria-label="Illustration of a connected car in a night city with network icons above">
    <defs><linearGradient id="g3" x1="0" y1="0" x2="1" y2="1"><stop offset="0" stop-color="#2f6fc0"/><stop offset=".5" stop-color="#123d7a"/><stop offset="1" stop-color="#061a3d"/></linearGradient></defs>
    <polygon points="45,0 207,0 207,177 45,177 0,88" fill="url(#g3)"/>
  </svg>
  <h2 class="abs h-title" style="left:27px;top:27px;font-size:18px">Introduction</h2>
  <p class="abs" style="left:27px;top:59px;font-size:8px;line-height:1.3;width:150px">This presentation outlines key insights, strategic direction, and opportunities within [topic/industry].</p>
  <ul class="abs" style="left:27px;top:107px;list-style:none;font-size:8px">
    <li style="height:22px;display:flex;align-items:center;gap:8px"><i style="width:5px;height:5px;background:var(--blue);display:block"></i>Key objective 1</li>
    <li style="height:22px;display:flex;align-items:center;gap:8px"><i style="width:5px;height:5px;background:var(--blue);display:block"></i>Key objective 2</li>
    <li style="height:22px;display:flex;align-items:center;gap:8px"><i style="width:5px;height:5px;background:var(--blue);display:block"></i>Key objective 3</li>
  </ul>
  <svg class="stripes" viewBox="0 0 50 100" aria-hidden="true"><use href="#stripe"/></svg>
</section>

<!-- 4 About the Company -->
<section class="slide" style="left:50px;top:251px;width:385px;height:173px">
  <div class="slide-num">4</div>
  <h2 class="abs h-title" style="left:34px;top:18px;font-size:16px">About the Company</h2>
  <div class="fact" style="top:50px"><svg width="30" height="27" aria-hidden="true"><use href="#hex-line" style="color:var(--navy)"/><use href="#ic-calendar" style="color:var(--navy)"/></svg><div><b>Founded</b><span>xxxx</span></div></div>
  <div class="fact" style="top:88px"><svg width="30" height="27" aria-hidden="true"><use href="#hex-line" style="color:var(--navy)"/><use href="#ic-building" style="color:var(--navy)"/></svg><div><b>Industry</b><span>xxxx</span></div></div>
  <div class="fact" style="top:124px"><svg width="30" height="27" aria-hidden="true"><use href="#hex-line" style="color:var(--navy)"/><use href="#ic-chart" style="color:var(--navy)"/></svg><div><b>Market Position</b><span>xxxx</span></div></div>
  <div class="vdiv" style="left:192px;top:24px;height:125px"></div>
  <h3 class="abs h-title" style="left:208px;top:20px;font-size:13px">Company Highlights</h3>
  <div class="strength" style="top:48px"><svg width="26" height="23" aria-hidden="true"><use href="#hex" style="color:var(--navy)"/><use href="#ic-trend" style="color:#fff"/></svg><p>Key strength 1:<br>Lorem ipsum dolor sit amet,<br>consectetur adipiscing elit.</p></div>
  <div class="strength" style="top:87px"><svg width="26" height="23" aria-hidden="true"><use href="#hex" style="color:var(--navy)"/><use href="#ic-bars" style="color:#fff"/></svg><p>Key strength 2<br>Lorem ipsum dolor sit amet,<br>consectetur adipiscing elit.</p></div>
  <div class="strength" style="top:126px"><svg width="26" height="23" aria-hidden="true"><use href="#hex" style="color:var(--blue)"/><use href="#ic-trend" style="color:#fff"/></svg><p>Key strength 3<br>Lorem ipsum dolor sit amet,<br>consectetur adipiscing elit.</p></div>
  <svg class="stripes" viewBox="0 0 50 100" aria-hidden="true"><use href="#stripe"/></svg>
</section>

<!-- 5 Challenges -->
<section class="slide" style="left:444px;top:251px;width:327px;height:173px">
  <div class="slide-num">5</div>
  <h2 class="abs h-title" style="left:38px;top:14px;font-size:15px">Challenges &amp; Opportunities</h2>
  <div class="challenge" style="top:44px"><svg width="32" height="28" aria-hidden="true"><use href="#hex" style="color:var(--navy)"/><use href="#ic-trend" style="color:#fff"/></svg><p>Current challenge or gap:<br>Addressing operational inefficiencies and evolving</p></div>
  <div class="challenge" style="top:85px"><svg width="32" height="28" aria-hidden="true"><use href="#hex" style="color:var(--navy)"/><use href="#ic-bars" style="color:#fff"/></svg><p>Market shift or trend: Industry transformation driven by technology and changing market</p></div>
  <div class="challenge" style="top:123px"><svg width="32" height="28" aria-hidden="true"><use href="#hex" style="color:var(--blue)"/><use href="#ic-trend" style="color:#fff"/></svg><p>Opportunity for growth: Leverage innovation and strategic partnerships to unlock long-term</p></div>
  <svg class="stripes" viewBox="0 0 50 100" aria-hidden="true"><use href="#stripe"/></svg>
</section>

<!-- 6 Proposed Strategy -->
<section class="slide" style="left:780px;top:251px;width:375px;height:173px">
  <div class="slide-num">6</div>
  <h2 class="abs h-title" style="left:33px;top:17px;font-size:15px">Proposed Strategy</h2>
  <div class="pillar" style="left:12px"><svg width="44" height="39" aria-hidden="true"><use href="#hex" style="color:var(--navy)"/><use href="#ic-people" style="color:#fff"/></svg><p>Strategy Pillar 1:<br>Focus on<br>customer<br>experience and</p></div>
  <div class="vdiv" style="left:93px;top:48px;height:95px"></div>
  <div class="pillar" style="left:97px"><svg width="44" height="39" aria-hidden="true"><use href="#hex" style="color:var(--blue)"/><use href="#ic-shake" style="color:#fff"/></svg><p>Strategy Pillar 1:<br>Focus on<br>customer<br>experience and</p></div>
  <div class="vdiv" style="left:178px;top:48px;height:95px"></div>
  <div class="pillar" style="left:182px"><svg width="44" height="39" aria-hidden="true"><use href="#hex" style="color:var(--blue)"/><use href="#ic-trend" style="color:#fff"/></svg><p>Strategy Pillar 1:<br>Focus on<br>customer<br>experience and</p></div>
  <div class="vdiv" style="left:261px;top:48px;height:95px"></div>
  <div class="pillar" style="left:264px"><svg width="44" height="39" aria-hidden="true"><use href="#hex" style="color:var(--navy)"/><use href="#ic-people" style="color:#fff"/></svg><p>Strategy Pillar 1:<br>Focus on<br>customer<br>experience and</p></div>
  <svg class="stripes" viewBox="0 0 50 100" aria-hidden="true"><use href="#stripe"/></svg>
</section>

<!-- 7 Key insights -->
<section class="slide" style="left:50px;top:432px;width:385px;height:170px">
  <div class="slide-num">7</div>
  <h2 class="abs h-title" style="left:35px;top:13px;font-size:15px">Key insights</h2>
  <p class="abs" style="left:35px;top:40px;font:500 6.8px/1.2 Roboto,sans-serif;color:var(--navy)">The following data highlights performance<br>trend and strategic implications</p>
  <p class="abs" style="left:60px;top:62px;font:500 7.5px Roboto,sans-serif;color:var(--navy)">Revenue Growth (in-%M)</p>
  <svg class="abs" style="left:10px;top:70px" width="190" height="90" viewBox="0 0 190 90" aria-label="Bar chart of revenue growth 2021 to 2025" role="img">
    <g font-family="Roboto" font-size="8.5" fill="#16243f" text-anchor="end">
      <text x="22" y="14">100</text><text x="22" y="29.5">75</text><text x="22" y="45">50</text><text x="22" y="60.5">25</text><text x="22" y="76">0</text>
    </g>
    <line x1="27" y1="8" x2="27" y2="73" stroke="#16243f" stroke-width=".7"/>
    <line x1="27" y1="73" x2="176" y2="73" stroke="#16243f" stroke-width=".7"/>
    <g fill="#1f5fb3">
      <rect x="33" y="45" width="16" height="28"/><rect x="62" y="39" width="16" height="34"/><rect x="92" y="33" width="16" height="40"/><rect x="121" y="26.5" width="16" height="46.5"/><rect x="152" y="20.3" width="16" height="52.7"/>
    </g>
    <g font-family="Roboto" font-size="8.5" fill="#16243f" text-anchor="middle">
      <text x="41" y="42">45</text><text x="70" y="36">55</text><text x="100" y="30">65</text><text x="129" y="23.5">75</text><text x="160" y="17.3">85</text>
    </g>
    <g font-family="Roboto" font-size="7.5" fill="#16243f" text-anchor="middle">
      <text x="41" y="84">2021</text><text x="70" y="84">2022</text><text x="100" y="84">2023</text><text x="129" y="84">2024</text><text x="160" y="84">2025</text>
    </g>
  </svg>
  <svg class="abs" style="left:200px;top:69px" width="88" height="88" viewBox="0 0 88 88" role="img" aria-label="Donut chart split 40, 30, 20 and 10 percent">
    <g transform="rotate(-90 44 44)" fill="none" stroke-width="28">
      <circle cx="44" cy="44" r="28" stroke="#1f5fb3" stroke-dasharray="70.37 175.93"/>
      <circle cx="44" cy="44" r="28" stroke="#3a6ea8" stroke-dasharray="52.78 175.93" stroke-dashoffset="-70.37"/>
      <circle cx="44" cy="44" r="28" stroke="#55647a" stroke-dasharray="35.19 175.93" stroke-dashoffset="-123.15"/>
      <circle cx="44" cy="44" r="28" stroke="#8a93a3" stroke-dasharray="17.59 175.93" stroke-dashoffset="-158.34"/>
    </g>
    <g fill="none" stroke="#eef0f3" stroke-width="1.2"><circle cx="44" cy="44" r="42"/></g>
    <g font-family="Roboto" font-size="7.5" fill="#fff" text-anchor="middle">
      <text x="71" y="48">40%</text><text x="42" y="82">30%</text><text x="12" y="41">20%</text><text x="34" y="17">10%</text>
    </g>
  </svg>
  <ul class="legend">
    <li><i style="background:#1f5fb3"></i>text here</li>
    <li><i style="background:#3a6ea8"></i>text here</li>
    <li><i style="background:#55647a"></i>text here</li>
    <li><i style="background:#8a93a3"></i>text here</li>
  </ul>
  <svg class="stripes" viewBox="0 0 50 100" aria-hidden="true"><use href="#stripe"/></svg>
</section>

<!-- 8 Key Responsibilities -->
<section class="slide" style="left:444px;top:432px;width:327px;height:170px">
  <div class="slide-num">8</div>
  <svg class="photo" style="left:195px;top:18px" width="132" height="120" viewBox="0 0 132 120" role="img" aria-label="Photo of business hands reviewing charts on paperwork">
    <defs><linearGradient id="g8" x1="0" y1="0" x2="1" y2="1"><stop offset="0" stop-color="#2c3d5c"/><stop offset=".55" stop-color="#7f93ad"/><stop offset="1" stop-color="#d7e0ea"/></linearGradient></defs>
    <polygon points="32,2 100,2 130,60 100,118 32,118 2,60" fill="url(#g8)" stroke="#1f5fb3" stroke-width="1.5"/>
  </svg>
  <h2 class="abs h-title" style="left:30px;top:14px;font-size:15px">Key Responsibilities</h2>
  <div class="resp" style="top:43px"><svg width="11" height="11" viewBox="0 0 12 12" aria-hidden="true"><polygon points="3,0 9,0 12,6 9,12 3,12 0,6" fill="var(--blue)"/><polyline points="3,6 5.3,8.2 9,4" fill="none" stroke="#fff" stroke-width="1.5"/></svg><p>Responsibility 1:<br>Lead strategic initiatives that drive growth and value.</p></div>
  <div class="resp" style="top:73px"><svg width="11" height="11" viewBox="0 0 12 12" aria-hidden="true"><polygon points="3,0 9,0 12,6 9,12 3,12 0,6" fill="var(--blue)"/><polyline points="3,6 5.3,8.2 9,4" fill="none" stroke="#fff" stroke-width="1.5"/></svg><p>Responsibility 1:<br>Lead strategic initiatives that drive growth and value.</p></div>
  <div class="resp" style="top:103px"><svg width="11" height="11" viewBox="0 0 12 12" aria-hidden="true"><polygon points="3,0 9,0 12,6 9,12 3,12 0,6" fill="var(--blue)"/><polyline points="3,6 5.3,8.2 9,4" fill="none" stroke="#fff" stroke-width="1.5"/></svg><p>Responsibility 1:<br>Lead strategic initiatives that drive growth and value.</p></div>
  <div class="resp" style="top:133px"><svg width="11" height="11" viewBox="0 0 12 12" aria-hidden="true"><polygon points="3,0 9,0 12,6 9,12 3,12 0,6" fill="var(--blue)"/><polyline points="3,6 5.3,8.2 9,4" fill="none" stroke="#fff" stroke-width="1.5"/></svg><p>Responsibility 1:<br>Lead strategic initiatives that drive growth and</p></div>
  <svg class="stripes" viewBox="0 0 50 100" aria-hidden="true"><use href="#stripe"/></svg>
</section>

<!-- 9 Value Proposition -->
<section class="slide" style="left:780px;top:432px;width:375px;height:170px">
  <div class="slide-num">9</div>
  <h2 class="abs h-title" style="left:36px;top:15px;font-size:15px">Value Proposition</h2>
  <div class="benefit" style="left:12px"><svg width="50" height="44" aria-hidden="true"><use href="#hex" style="color:var(--navy)"/><use href="#ic-people" style="color:#fff"/></svg><b>Benefit 1:</b><p>Deliver exceptional<br>value and quality<br>to our customers.</p></div>
  <div class="vdiv" style="left:120px;top:72px;height:80px"></div>
  <div class="benefit" style="left:121px"><svg width="50" height="44" aria-hidden="true"><use href="#hex" style="color:var(--blue)"/><use href="#ic-shake" style="color:#fff"/></svg><b>Benefit 1:</b><p>Deliver exceptional<br>value and quality<br>to our customers.</p></div>
  <div class="vdiv" style="left:231px;top:72px;height:80px"></div>
  <div class="benefit" style="left:228px"><svg width="50" height="44" aria-hidden="true"><use href="#hex" style="color:var(--blue)"/><use href="#ic-trend" style="color:#fff"/></svg><b>Benefit 1:</b><p>Deliver exceptional<br>value and quality<br>to our customers.</p></div>
  <svg class="stripes" viewBox="0 0 50 100" aria-hidden="true"><use href="#stripe"/></svg>
</section>

<!-- 10 Timeline -->
<section class="slide" style="left:50px;top:610px;width:385px;height:166px">
  <div class="slide-num">10</div>
  <h2 class="abs h-title" style="left:40px;top:12px;font-size:15px">Timeline / Roadmap</h2>
  <svg class="abs" style="left:20px;top:52px" width="340" height="10" aria-hidden="true"><line x1="4" y1="5" x2="335" y2="5" stroke="var(--navy)" stroke-width="1.4"/><rect x="1" y="2" width="6" height="6" fill="var(--navy)"/><rect x="332" y="2" width="6" height="6" fill="var(--navy)"/></svg>
  <div class="phase" style="left:31px;top:37px"><svg width="42" height="37" aria-hidden="true"><use href="#hex-line" style="color:var(--navy)"/><use href="#ic-people" style="color:var(--navy)"/></svg><b>Phase 1:</b><p>FoundationBuild<br>the foundation and<br>align key initiatives.</p></div>
  <div class="phase" style="left:142px;top:37px"><svg width="42" height="37" aria-hidden="true"><use href="#hex-line" style="color:var(--navy)"/><use href="#ic-shake" style="color:var(--navy)"/></svg><b>Phase 1:</b><p>FoundationBuild<br>the foundation and<br>align key initiatives.</p></div>
  <div class="phase" style="left:250px;top:37px"><svg width="42" height="37" aria-hidden="true"><use href="#hex-line" style="color:var(--navy)"/><use href="#ic-trend" style="color:var(--navy)"/></svg><b>Phase 1:</b><p>FoundationBuild<br>the foundation and<br>align key initiatives.</p></div>
  <svg class="stripes" viewBox="0 0 50 100" aria-hidden="true"><use href="#stripe"/></svg>
</section>

<!-- 11 Next Steps -->
<section class="slide" style="left:444px;top:610px;width:327px;height:166px">
  <div class="slide-num">11</div>
  <svg class="abs" style="left:0;top:0" width="327" height="166" viewBox="0 0 327 166" aria-hidden="true"><polygon points="270,0 327,0 327,166 240,166" fill="var(--navy)"/></svg>
  <svg class="photo" style="left:168px;top:2px" width="150" height="136" viewBox="0 0 150 136" role="img" aria-label="Photo of two business people shaking hands">
    <defs><linearGradient id="g11" x1="0" y1="0" x2="1" y2="1"><stop offset="0" stop-color="#9fb2c6"/><stop offset=".5" stop-color="#4d6584"/><stop offset="1" stop-color="#1a2a45"/></linearGradient></defs>
    <polygon points="38,2 112,2 148,68 112,134 38,134 2,68" fill="url(#g11)" stroke="#fff" stroke-width="3"/>
  </svg>
  <h2 class="abs h-title" style="left:23px;top:37px;font-size:16px">Next Steps</h2>
  <p class="abs" style="left:20px;top:68px;font-size:8.5px;line-height:1.35">We invite you to take the next<br>step and engage with this</p>
  <div class="cta">CONTACT US</div>
</section>

<!-- 12 Thank You -->
<section class="slide" style="left:780px;top:610px;width:375px;height:166px">
  <div class="slide-num">12</div>
  <div class="brand" style="left:28px;top:33px;font-size:11.5px"><i class="mark"></i>Arvenhold Executive</div>
  <h2 class="abs" style="left:28px;top:70px;font:700 22px 'Exo 2',sans-serif;color:var(--navy-deep)">Thank You</h2>
  <div class="abs" style="left:30px;top:107px;width:20px;height:2px;background:var(--blue)"></div>
  <div class="vdiv" style="left:171px;top:38px;height:80px;background:#c9d1dd"></div>
  <div class="contact" style="top:40px"><svg width="10" height="10" viewBox="0 0 10 10" aria-hidden="true"><path d="M2 0.5h2l1 2.3-1.3 1a6 6 0 0 0 2.5 2.5l1-1.3 2.3 1v2a1 1 0 0 1-1 1A8.5 8.5 0 0 1 1 1.5a1 1 0 0 1 1-1z" fill="var(--navy)"/></svg>+1 555 014 2290</div>
  <div class="contact" style="top:60px"><svg width="10" height="10" viewBox="0 0 10 10" aria-hidden="true"><rect x=".7" y="2" width="8.6" height="6" fill="none" stroke="var(--navy)" stroke-width="1"/><polyline points=".7,2 5,5.5 9.3,2" fill="none" stroke="var(--navy)" stroke-width="1"/></svg>info@arvenhold-example.com</div>
  <div class="contact" style="top:80px"><svg width="10" height="10" viewBox="0 0 10 10" aria-hidden="true"><g fill="none" stroke="var(--navy)" stroke-width=".9"><circle cx="5" cy="5" r="4.2"/><ellipse cx="5" cy="5" rx="1.8" ry="4.2"/><line x1=".8" y1="5" x2="9.2" y2="5"/></g></svg>www.arvenhold-example.com</div>
  <div class="contact" style="top:101px"><svg width="10" height="11" viewBox="0 0 10 11" aria-hidden="true"><path d="M5 0.5a3.6 3.6 0 0 1 3.6 3.6C8.6 7 5 10.5 5 10.5S1.4 7 1.4 4.1A3.6 3.6 0 0 1 5 .5z" fill="var(--navy)"/><circle cx="5" cy="4.1" r="1.3" fill="#fff"/></svg><span>48 Meridian Row,<br>Harbor City, HC 20417</span></div>
  <svg class="stripes" viewBox="0 0 50 100" aria-hidden="true"><use href="#stripe"/></svg>
</section>

</body>
</html>
```